needs to stand out, but be very clean
Project: Logo for auto broker stationary,
Logo for auto broker stationary,  - Automotive
Logo for auto broker stationary,
Professional
Harbor Motorworks USA
Los Angeles based, Global shipping
Dorian@harbormotorworks-example.com
www.harbormotorworks-example.com
I would like to have at least one file in vector eps, logo and cards. I would like 4 or 6 automotive logos in the corners (4) velorian, Kastra, Tenko, Ardello or (6) Velorian, Kastra, Ardello, Tenko, Ardello, Quellano the other two in the middle of top and bottom. If you like the initials HMU you can use them. working on getting 800 number now, please just put in 555-014-2731 and we can change it later. I was thinking black background for card with white or silver writing and maybe some kind of splash of red.
Pick a font or style you like saying: You don't go to court without an attorney. Why would you buy a car without your Broker?
DorianPlume DorianPlume
I'm surprised that only one person actually read what I wrote and showed me one business card with car logos (kastra, velorian etc. ) on it. I think I like the logo centered.

```html
<!DOCTYPE html>
<html lang="en">
<head>
<meta charset="utf-8">
<title>Harbor Motorworks USA — Business Card</title>
<link rel="stylesheet" href="https://fonts.googleapis.com/css2?family=Cinzel:wght@600&family=Open+Sans:wght@400;600;700&display=swap">
<style>
  :root {
    --stage: #3a3a3c;
    --card-black: #222224;
    --card-black-edge: #2e2e30;
    --card-white: #f4f4f4;
    --card-white-shade: #e2e2e2;
    --brand-red: #d8141c;
    --band-dark: #333335;
    --ink-dark: #2a2a2a;
    --ink-grey: #6d6d6d;
    --ink-light: #e8e8e8;
    --serif: "Cinzel", "Times New Roman", serif;
    --sans: "Open Sans", Arial, sans-serif;
  }
  * { box-sizing: border-box; margin: 0; padding: 0; }
  html, body { width: 1200px; height: 670px; overflow: hidden; }
  body { background: var(--stage); position: relative; font-family: var(--sans); }

  .card {
    position: absolute;
    width: 520px;
    height: 297px;
    border-radius: 3px;
    overflow: hidden;
    box-shadow: 0 10px 24px rgba(0,0,0,.35);
  }

  /* Front */
  .card-front {
    left: 60px; top: 70px;
    background: linear-gradient(135deg, var(--card-black-edge), var(--card-black));
    display: flex; align-items: center; justify-content: center;
  }
  .wordmark {
    display: flex; align-items: center; gap: 12px;
    font-family: var(--serif); font-weight: 600;
    letter-spacing: .04em; text-transform: uppercase;
    white-space: nowrap;
  }
  .wordmark-dot { width: 12px; height: 12px; border-radius: 50%; background: var(--brand-red); flex: none; }
  .card-front .wordmark { color: #ffffff; font-size: 26px; }

  /* Back */
  .card-back {
    left: 620px; top: 300px;
    background: linear-gradient(160deg, var(--card-white), var(--card-white-shade));
  }
  .card-back .wave { position: absolute; inset: 0; }
  .card-back .wordmark { position: absolute; left: 34px; top: 52px; color: var(--ink-dark); font-size: 19px; }
  .card-back .wordmark-dot { width: 10px; height: 10px; }

  .holder { position: absolute; left: 36px; top: 150px; }
  .holder-name { color: var(--brand-red); font-weight: 700; font-size: 14px; letter-spacing: .03em; text-transform: uppercase; }
  .holder-title { color: var(--ink-grey); font-size: 10px; margin-top: 2px; }

  .address {
    position: absolute; right: 24px; top: 30px;
    text-align: right; color: var(--ink-grey); font-size: 9px; line-height: 1.5;
  }
  .contact {
    position: absolute; right: 24px; top: 194px;
    list-style: none; text-align: right;
    color: var(--ink-light); font-size: 9px; line-height: 1.95;
    white-space: nowrap;
  }
  .contact li { display: flex; justify-content: flex-end; align-items: center; gap: 6px; }
  .contact svg { width: 9px; height: 9px; fill: var(--ink-light); flex: none; }
</style>
</head>
<body>

  <section class="card card-front" aria-label="Card front">
    <div class="wordmark"><span class="wordmark-dot"></span><span>Harbor Motorworks USA</span></div>
  </section>

  <section class="card card-back" aria-label="Card back">
    <svg class="wave" viewBox="0 0 520 297" preserveAspectRatio="none" aria-hidden="true">
      <path d="M0 215 C120 250 230 200 300 160 C380 115 460 90 520 80 L520 297 L0 297 Z" fill="var(--brand-red)"/>
      <path d="M0 233 C120 268 230 218 300 178 C380 133 460 108 520 98 L520 297 L0 297 Z" fill="var(--band-dark)"/>
    </svg>

    <div class="wordmark"><span class="wordmark-dot"></span><span>Harbor Motorworks USA</span></div>

    <div class="holder">
      <p class="holder-name">Dorian Plume</p>
      <p class="holder-title">Managing Director</p>
    </div>

    <p class="address">214 Harbor Ave West<br>Los Angeles CA 90012</p>

    <ul class="contact">
      <li>555-014-2731
        <svg viewBox="0 0 24 24"><path d="M6.6 10.8a15 15 0 0 0 6.6 6.6l2.2-2.2a1 1 0 0 1 1-.25 11 11 0 0 0 3.6.6 1 1 0 0 1 1 1V20a1 1 0 0 1-1 1A17 17 0 0 1 3 4a1 1 0 0 1 1-1h3.5a1 1 0 0 1 1 1 11 11 0 0 0 .6 3.6 1 1 0 0 1-.25 1z"/></svg>
      </li>
      <li>Dorian@harbormotorworks-example.com
        <svg viewBox="0 0 24 24"><path d="M2 5h20v14H2zm2 2v.4l8 5 8-5V7z"/></svg>
      </li>
      <li>www.harbormotorworks-example.com
        <svg viewBox="0 0 24 24"><circle cx="12" cy="12" r="10"/></svg>
      </li>
    </ul>
  </section>

</body>
</html>
```